Tick Tock Green Frog

I'm looking for one generic business card that be used for four people or would it be easier to get four different design of cards.

I have attached the logo, of the cow. I would also like to use one colour of the cow's legs in the background.

Info for card:
Dana Holcroft
Wrangler of Opportunities
Phone: 044 718 2094
email: dana.holcroft@ticktockgreenfrogs.com.au
Web: www.ticktockgreenfrogs.com.au

Here is some tag lines that could also be used:

"Guiding you in the right direction"

"Putting the Tick Tock back into early childhood"
"Where's there is NO bull"

Industry/Entity Type

Business

```html
<!DOCTYPE html>
<html lang="en">
<head>
<meta charset="utf-8">
<title>Tick Tock Green Frog – Business Card</title>
<link rel="stylesheet" href="https://fonts.googleapis.com/css2?family=Boogaloo&family=Open+Sans:wght@300;400;700&family=Varela+Round&display=swap">
<style>
  :root {
    --page-bg: #e4e4e4;
    --card-white: #ffffff;
    --card-green: #669900;
    --brown: #4a2508;
    --brown-light: #7a4a1e;
    --orange: #f26d1f;
    --ink: #4d4d4d;
    --lime: #c8e64a;
    --shadow: rgba(0, 0, 0, 0.18);
  }
  * { box-sizing: border-box; margin: 0; padding: 0; }
  html, body {
    width: 1200px;
    height: 960px;
    overflow: hidden;
    background: var(--page-bg);
  }
  .sheet {
    width: 1200px;
    height: 960px;
    display: flex;
    flex-direction: column;
    align-items: center;
    justify-content: center;
    gap: 50px;
  }
  .card {
    position: relative;
    width: 680px;
    height: 415px;
    overflow: hidden;
    box-shadow: 0 6px 18px var(--shadow);
  }

  /* Front */
  .card--front { background: var(--card-white); }
  .card-front__mascot {
    position: absolute;
    left: 0;
    bottom: 0;
    width: 210px;
    height: 200px;
    background: linear-gradient(160deg, var(--brown-light), var(--brown));
  }
  .card-front__details {
    position: absolute;
    left: 260px;
    top: 78px;
    width: 380px;
  }
  .person-name {
    font-family: "Boogaloo", cursive;
    font-size: 42px;
    line-height: 1;
    color: var(--brown);
  }
  .person-role {
    font-family: "Open Sans", sans-serif;
    font-weight: 300;
    font-size: 16px;
    letter-spacing: 0.5px;
    color: var(--ink);
    margin-top: 8px;
    padding-bottom: 14px;
    border-bottom: 2px solid var(--orange);
  }
  .contact-list {
    list-style: none;
    margin-top: 48px;
    font-family: "Open Sans", sans-serif;
    font-weight: 300;
    font-size: 16px;
    line-height: 1.45;
    color: var(--ink);
  }
  .contact-list__label { display: inline-block; width: 22px; }
  .web-address {
    margin-top: 28px;
    font-family: "Open Sans", sans-serif;
    font-weight: 700;
    font-size: 17px;
    color: var(--orange);
  }

  /* Back */
  .card--back {
    background: var(--card-green);
    display: flex;
    flex-direction: column;
    align-items: center;
    justify-content: center;
    gap: 36px;
  }
  .brand {
    display: flex;
    align-items: center;
    gap: 18px;
  }
  .brand__dot {
    width: 46px;
    height: 46px;
    border-radius: 50%;
    background: var(--brown);
  }
  .brand__name {
    font-family: "Varela Round", sans-serif;
    font-size: 44px;
    color: var(--card-white);
  }
  .tagline {
    font-family: "Varela Round", sans-serif;
    font-size: 22px;
    color: var(--lime);
  }
</style>
</head>
<body>
  <main class="sheet">
    <section class="card card--front" aria-label="Business card front">
      <div class="card-front__mascot" role="img" aria-label="Brand mascot illustration peeking in from the lower left corner"></div>
      <div class="card-front__details">
        <h1 class="person-name">Dana Holcroft</h1>
        <p class="person-role">WRANGLER OF OPPORTUNITIES</p>
        <ul class="contact-list">
          <li><span class="contact-list__label">P:</span>044 718 2094</li>
          <li><span class="contact-list__label">E:</span>dana.holcroft@ticktockgreenfrogs.com.au</li>
        </ul>
        <p class="web-address">www.ticktockgreenfrogs.com.au</p>
      </div>
    </section>

    <section class="card card--back" aria-label="Business card back">
      <div class="brand">
        <span class="brand__dot"></span>
        <span class="brand__name">Tick Tock Green Frog</span>
      </div>
      <p class="tagline">Guiding you in the right direction</p>
    </section>
  </main>
</body>
</html>
```